Modern Retail Coffee Label for established Roastery! 17 years!

We are looking for a Retail Coffee Bag Label... JUST THE LABEL TO GO ON AN EXISTING BAG. Our current label is provided and our Logo.. we have had the same Red Bags FOREVER so we are looking for a label to compliment that tradition and to be placed on the bags we have used for 17 years.

We have a retail line of bags with locally roasted coffee. Our business has been around 17years and is in need of a design upgrade! We have a red coffee bag and are looking for a sleek modern label. I will attach a file of our label right now so you can see what it looks like. We are just looking for a more modern version. a few inclusions:

Locally Roasted
100% Arabica Coffee
Heron Kin's Coffee
heronkincoffee.example
logo

The black label with the red and yellow color label is the old one... the new label should be the White background and black border one...

Target Market(s)

Retail Coffee Consumers

Font styles to use
Other font styles liked:
• use what you think. we are located in SW Wisconsin but ship coffee EVERYWHERE

Colors

Designer to choose only greyscale colors for use in the design.

Requirements
Must have
• Locally Roasted (Platteville,WI)
• 100% Arabica Coffee
• heronkincoffee.example
• logo
Nice to have
• Badgers
• "Since 2003"
Should not have
• Any lunabrew or big brand themes

```html
<!DOCTYPE html>
<html lang="en">
<head>
<meta charset="utf-8">
<title>Heron Kin's Coffee – Retail Bag Label</title>
<link rel="stylesheet" href="https://fonts.googleapis.com/css2?family=Oswald:wght@400;500;600;700&display=swap">
<style>
  :root {
    --backdrop: #dcae94;
    --label-black: #0b0a09;
    --tan: #e4a47f;
    --tan-light: #eab796;
    --brown: #6e3b2b;
    --frame-grey: #6a6664;
    --rule: #8a5e44;
    --white: #ffffff;
    --pattern-light: #e8c29c;
    --pattern-mid: #a4714f;
    --pattern-dark: #4a2a1d;
  }
  * { margin: 0; padding: 0; box-sizing: border-box; }
  html, body {
    width: 960px;
    height: 1200px;
    overflow: hidden;
    background: var(--backdrop);
  }
  .label {
    position: absolute;
    left: 60px;
    top: 40px;
    width: 840px;
    height: 1120px;
    background: var(--label-black);
    font-family: "Oswald", "Arial Narrow", sans-serif;
  }
  .brand-plate {
    position: absolute;
    left: 260px;
    top: 0;
    width: 320px;
    height: 243px;
    background: var(--white);
    border-radius: 0 0 14px 14px;
    display: flex;
    align-items: center;
    justify-content: center;
  }
  .brand-name {
    font-weight: 600;
    font-size: 46px;
    line-height: 1.1;
    color: var(--label-black);
    text-align: center;
    text-transform: uppercase;
    letter-spacing: 1px;
  }
  .title-frame {
    position: absolute;
    left: 82px;
    top: 304px;
    width: 676px;
    height: 502px;
    border: 2px solid var(--frame-grey);
    border-radius: 14px;
  }
  .title-line {
    position: absolute;
    left: 38px;
    font-weight: 700;
    letter-spacing: -2px;
    line-height: 1;
    transform-origin: left top;
    white-space: nowrap;
  }
  .title-first {
    top: 30px;
    font-size: 210px;
    color: var(--tan-light);
    transform: scaleX(0.84);
  }
  .title-second {
    top: 238px;
    font-size: 150px;
    color: var(--brown);
    transform: scaleX(0.9);
  }
  .title-vertical {
    position: absolute;
    left: 492px;
    top: 44px;
    width: 146px;
    height: 356px;
    display: flex;
    align-items: center;
    justify-content: center;
  }
  .title-vertical span {
    display: block;
    transform: rotate(-90deg) scaleX(0.9);
    font-weight: 700;
    font-size: 150px;
    line-height: 1;
    color: var(--tan);
    white-space: nowrap;
  }
  .web-row {
    position: absolute;
    left: 44px;
    right: 44px;
    top: 432px;
    display: flex;
    align-items: center;
    gap: 18px;
  }
  .web-row .rule { flex: 1; height: 1px; background: var(--rule); }
  .web-address {
    font-weight: 400;
    font-size: 21px;
    color: var(--tan-light);
    letter-spacing: 0.5px;
  }
  .roast-block {
    position: absolute;
    left: 0;
    right: 0;
    top: 830px;
    display: flex;
    flex-direction: column;
    align-items: center;
  }
  .roast-line {
    display: flex;
    align-items: flex-end;
    gap: 4px;
  }
  .roast-locally {
    writing-mode: vertical-rl;
    transform: rotate(180deg);
    font-size: 22px;
    font-weight: 400;
    color: var(--brown);
    line-height: 1;
    margin-bottom: 4px;
  }
  .roast-word {
    font-size: 82px;
    font-weight: 500;
    color: var(--white);
    line-height: 1;
    letter-spacing: -2px;
  }
  .roast-sub {
    margin-top: 6px;
    font-size: 28px;
    font-weight: 600;
    color: var(--tan);
    line-height: 1;
  }
  .roast-rule {
    position: absolute;
    top: 910px;
    height: 2px;
    width: 180px;
    background: var(--rule);
  }
  .roast-rule-left { left: 82px; }
  .roast-rule-right { right: 82px; }
  .pattern-band {
    position: absolute;
    left: 0;
    bottom: 0;
    width: 840px;
    height: 122px;
    background: linear-gradient(90deg, var(--pattern-mid), var(--pattern-light) 30%, var(--pattern-dark) 55%, var(--pattern-light) 80%, var(--pattern-mid));
  }
</style>
</head>
<body>
  <main class="label">
    <div class="brand-plate">
      <p class="brand-name">Heron Kin<br>Coffee</p>
    </div>

    <section class="title-frame">
      <h1>
        <span class="title-line title-first">Heron</span>
        <span class="title-line title-second">Kin's</span>
        <span class="title-vertical"><span>Coffee</span></span>
      </h1>
      <div class="web-row">
        <span class="rule"></span>
        <span class="web-address">heronkincoffee.example</span>
        <span class="rule"></span>
      </div>
    </section>

    <span class="roast-rule roast-rule-left"></span>
    <span class="roast-rule roast-rule-right"></span>
    <div class="roast-block">
      <div class="roast-line">
        <span class="roast-locally">Locally</span>
        <span class="roast-word">Roasted</span>
      </div>
      <p class="roast-sub">100% Arabica Coffee</p>
    </div>

    <div class="pattern-band" role="img" aria-label="Decorative band of flowing swirl pattern in coffee browns and cream"></div>
  </main>
</body>
</html>
```